body therapist

I need to offer my services as a massage therapist at home, acclimating customer space aroma candles with music and everything else to bring comfort. 8 offer rituals like this: relaxing ritual, purifying ritual, ritual breast, facial and body cleansing ritual organic, ritual man, ritual feet, slimming ritual. Naraja handling colors, seawater, green, lavender

Target Market(s)

men and women, tired, stressed, looking for something new

Font styles to use
Decorative
Script

Colors
f37122
0493ce
abd037

Requirements
Must have
• detailing each massage
Nice to have
• simple and elegant

```html
<!DOCTYPE html>
<html lang="es">
<head>
<meta charset="utf-8">
<title>Rituales y Experiencias Spa – Folleto</title>
<link href="https://fonts.googleapis.com/css2?family=Cinzel+Decorative:wght@700&family=Dancing+Script:wght@600&family=Didact+Gothic&display=swap" rel="stylesheet">
<style>
  :root {
    --backdrop: #3f3f3f;
    --paper: #ffffff;
    --panel: #f1f2f2;
    --lime: #abd037;
    --lime-light: #c4de4f;
    --orange: #f37122;
    --sea: #0493ce;
    --orchid: #c94fc4;
    --ink: #555555;
    --shadow: rgba(0,0,0,0.35);
  }
  * { box-sizing: border-box; margin: 0; padding: 0; }
  html, body { width: 1200px; height: 1200px; overflow: hidden; }
  body {
    background: var(--backdrop);
    font-family: "Didact Gothic", "Century Gothic", sans-serif;
    color: var(--ink);
    position: relative;
  }
  .spread {
    position: absolute;
    left: 20px; top: 185px;
    width: 1160px; height: 830px;
    display: flex;
    box-shadow: 0 20px 50px var(--shadow);
  }
  .page {
    position: relative;
    width: 580px; height: 830px;
    background: var(--paper);
    overflow: hidden;
  }
  .page--left::after, .page--right::after {
    content: ""; position: absolute; top: 0; bottom: 0; width: 40px; z-index: 5; pointer-events: none;
  }
  .page--left::after { right: 0; background: linear-gradient(90deg, rgba(0,0,0,0) 0%, rgba(0,0,0,0.18) 100%); }
  .page--right::after { left: 0; background: linear-gradient(90deg, rgba(0,0,0,0.15) 0%, rgba(0,0,0,0) 100%); }

  .floral-strip {
    position: absolute; left: 0; top: 0; width: 100%; height: 190px;
    background:
      linear-gradient(90deg, rgba(123,168,58,0.8) 0%, rgba(156,194,90,0.7) 30%, rgba(215,181,230,0.8) 55%, rgba(201,160,220,0.8) 70%, rgba(143,184,74,0.8) 100%) 0 95px / 100% 55px no-repeat,
      linear-gradient(180deg, #ffffff 0%, #eef0ee 55%, #e3e6dc 100%);
  }
  .page-number {
    position: absolute; top: -18px; width: 46px; height: 46px;
    border-radius: 50%; background: #e6e6e6;
    font-size: 14px; color: var(--sea); text-align: center; line-height: 60px;
    z-index: 3;
  }
  .page-number--left { left: 210px; }
  .page-number--right { left: 150px; }
  .lime-band { position: absolute; background: var(--lime); }
  .lime-band--left { left: 40px; top: 220px; width: 420px; height: 560px; }
  .lime-band--top { left: 0; top: 190px; width: 340px; height: 80px; }
  .lime-band--side { left: 450px; top: 150px; width: 130px; height: 440px; }
  .photo { position: absolute; }
  .photo--candle {
    left: 290px; top: 200px; width: 290px; height: 630px;
    background: radial-gradient(circle at 50% 42%, #fff7ea 0%, #f6c9b2 28%, #e98a95 48%, #e8b99a 70%, #f1d2bd 100%);
  }
  .photo--stones {
    left: 0; top: 270px; width: 420px; height: 560px;
    background: linear-gradient(180deg, #b9a4a6 0%, #7a6a7c 35%, #4a4350 60%, #8d8592 100%);
  }
  .panel {
    position: absolute; background: var(--panel);
    padding: 26px 22px;
    z-index: 2;
  }
  .panel--rituals { left: 100px; top: 170px; width: 330px; height: 630px; }
  .panel--experiences { left: 300px; top: 115px; width: 262px; height: 470px; }
  .panel-title {
    font-family: "Cinzel Decorative", serif; font-weight: 700;
    color: var(--orchid); line-height: 1;
    text-transform: uppercase;
  }
  .panel--rituals .panel-title { font-size: 33px; margin-bottom: 18px; }
  .panel--experiences .panel-title { font-size: 20px; text-align: center; margin-bottom: 18px; }
  .service-list { list-style: none; }
  .service {
    position: relative; padding-left: 20px; margin-bottom: 8px;
  }
  .service::before {
    content: ""; position: absolute; left: 0; top: 4px;
    width: 10px; height: 10px; background: var(--orange);
  }
  .service-name {
    display: block; font-size: 14px; line-height: 1.3; text-transform: uppercase; color: var(--ink);
  }
  .service-detail {
    display: block; font-size: 12px; line-height: 1.3; color: var(--sea);
  }
  .ritual-note {
    margin-top: 16px; font-size: 13px; line-height: 1.4;
    text-transform: uppercase; padding-right: 6px;
  }
  .duration-tag {
    position: absolute; background: var(--lime-light);
    color: #fff; font-family: "Dancing Script", cursive; font-weight: 600;
    font-size: 24px; line-height: 1.1; padding: 10px 18px; z-index: 3;
  }
  .duration-tag--rituals { left: 70px; top: 710px; width: 240px; }
  .duration-tag--experiences { left: 410px; top: 540px; width: 160px; text-align: center; }
</style>
</head>
<body>
  <main class="spread">
    <section class="page page--left">
      <div class="floral-strip" role="img" aria-label="Orquídeas lilas sobre tallos de bambú y piedra negra"></div>
      <span class="page-number page-number--left">4</span>
      <div class="lime-band lime-band--left"></div>
      <div class="photo photo--candle" role="img" aria-label="Vela blanca encendida junto a una flor rosa"></div>
      <article class="panel panel--rituals">
        <h2 class="panel-title">Rituales<br>Alborada</h2>
        <ul class="service-list">
          <li class="service"><span class="service-name">Ritual purificante</span><span class="service-detail">Exfoliación y masaje drenante que limpia la piel.</span></li>
          <li class="service"><span class="service-name">Ritual vinoterapia</span><span class="service-detail">Envoltura de uva y masaje relajante antioxidante.</span></li>
          <li class="service"><span class="service-name">Ritual mamá</span><span class="service-detail">Masaje suave y seguro para futuras mamás.</span></li>
          <li class="service"><span class="service-name">Ritual wellness pies</span><span class="service-detail">Reflexología y baño tibio de pies con sales.</span></li>
          <li class="service"><span class="service-name">Ritual de vitalidad para él</span><span class="service-detail">Masaje descontracturante de espalda y cuello.</span></li>
          <li class="service"><span class="service-name">Ritual pareja Alborada spa</span><span class="service-detail">Masaje relajante a cuatro manos, en pareja.</span></li>
        </ul>
        <p class="ritual-note">Todos nuestros rituales incluyen masaje facial con aromaterapia, ambientación con velas, aromas y musicoterapia</p>
      </article>
      <div class="duration-tag duration-tag--rituals">Entre una y dos horas aprox</div>
    </section>

    <section class="page page--right">
      <div class="floral-strip" role="img" aria-label="Orquídeas lilas y tallos de bambú con piedra negra"></div>
      <span class="page-number page-number--right">5</span>
      <div class="lime-band lime-band--top"></div>
      <div class="lime-band lime-band--side"></div>
      <div class="photo photo--stones" role="img" aria-label="Piedras negras apiladas sobre fondo lavanda"></div>
      <article class="panel panel--experiences">
        <h2 class="panel-title">Experiencias<br>Spa</h2>
        <ul class="service-list">
          <li class="service"><span class="service-name">Chocolaterapia</span><span class="service-detail">Envoltura de cacao hidratante.</span></li>
          <li class="service"><span class="service-name">Elixir de uva</span><span class="service-detail">Masaje con aceite de semilla de uva.</span></li>
          <li class="service"><span class="service-name">Exfoliación cítrica</span><span class="service-detail">Pulido con sales y naranja.</span></li>
          <li class="service"><span class="service-name">Exfoliación frutos rojos</span><span class="service-detail">Peeling suave antioxidante.</span></li>
          <li class="service"><span class="service-name">Sueños Alborada</span><span class="service-detail">Masaje con piedras calientes.</span></li>
        </ul>
      </article>
      <div class="duration-tag duration-tag--experiences">90 minutes</div>
    </section>
  </main>
</body>
</html>
```